Emergency Medical Training and Events Company Business Needs Business Card Design

We are in need of a business card for our dynamic company expanding its customer base and need to be easily contacted and identified for when we visit with government officials, potential EMS / Fire agencies and county coordinators to arrange for training programs for first responders to better prepare them for critical thinking at critical incidents.

Target Market(s)

EMS/Fire and Event Promoters

Industry/Entity Type

Medical

Contact Information for Business Card

Two cards, comparable designs:

Martin K. Halvey, Principal, m.halvey@rvqtlo.com
Owen Tash, Event and Training Specialist, o.tash@rvqtlo.com

Font styles to use
Other font styles liked:
• Cambria

Colors

Designer to choose colors to be used in the design.

Requirements
Must have
• Company Logo, Spots for Name, Title, Phone Number, Email, Website
• A bullet list stating that we offer, QRB CPR and First Aid Instructors, Hold the Line Instructors, Event EMS, CME's, MCI Training and Planning. We prefer to have a black background for the card but if you can make a blue or white card stand out we would review that as well.
Should not have
• Tacky logos or special sayings ... simple, elegant, professional is the look we seek

```html
<!DOCTYPE html>
<html lang="en">
<head>
<meta charset="utf-8">
<title>RVQTLO Response Training – Business Cards</title>
<link href="https://fonts.googleapis.com/css2?family=Merriweather:wght@400;700;900&family=Montserrat:wght@500&display=swap" rel="stylesheet">
<style>
  :root{
    --navy:#0f2a4d;
    --red:#c8333a;
    --paper:#eeeeee;
    --stage:#efefef;
    --white:#ffffff;
    --ink:#2b3445;
  }
  *{box-sizing:border-box;margin:0;padding:0}
  html,body{width:1168px;height:1200px;overflow:hidden;background:var(--white)}
  body{position:relative;font-family:"Merriweather",Georgia,serif;color:var(--ink)}
  .stage{position:absolute;left:0;top:0;width:1168px;height:600px;background:var(--stage)}
  .card{position:absolute;top:99px;width:216px;height:404px;box-shadow:2px 4px 8px rgba(0,0,0,.18);overflow:hidden}
  .card--front{background:var(--paper)}
  .card--back{background:var(--navy);color:var(--white)}
  .brand-mini{position:absolute;top:36px;right:20px;display:flex;align-items:center;gap:5px;font-weight:900;font-size:10px;color:var(--navy);letter-spacing:.3px}
  .brand-mini .dot{width:14px;height:14px;border-radius:50%;background:var(--navy)}
  .person{position:absolute;left:18px;top:136px}
  .person__name{font-weight:700;font-size:9.5px;color:var(--navy);text-transform:uppercase;border-bottom:1px solid var(--navy);padding-bottom:1px;display:inline-block;letter-spacing:.3px}
  .person__title{font-size:6.5px;letter-spacing:1.6px;text-transform:uppercase;color:var(--navy);margin-top:3px;line-height:1.3;max-width:120px}
  .contact{position:absolute;left:18px;top:312px;font-size:6.2px;line-height:1.45;color:var(--ink)}
  .contact li{list-style:none;display:flex;gap:6px;align-items:flex-start}
  .contact svg{width:8px;height:8px;flex:none;margin-top:1px;fill:var(--navy)}
  .contact strong{font-weight:700;color:var(--navy);text-transform:uppercase;display:block;max-width:160px}
  .services{position:absolute;left:22px;top:34px;font-size:6.8px;line-height:1.5;text-transform:uppercase;letter-spacing:.2px}
  .services li{list-style:none;display:flex;align-items:center;gap:7px}
  .services li::before{content:"";width:5px;height:5px;border-radius:50%;background:var(--white)}
  .brand-center{position:absolute;left:0;right:0;top:150px;display:flex;flex-direction:column;align-items:center;gap:8px}
  .brand-center .dot{width:80px;height:80px;border-radius:50%;background:var(--white)}
  .brand-center span{font-weight:900;font-size:11px;letter-spacing:.5px;color:var(--white)}
  .website{position:absolute;left:0;right:0;top:360px;text-align:center;font-family:"Montserrat",Arial,sans-serif;font-size:8.5px;letter-spacing:1.6px}
  .website svg{display:block;margin:0 auto 6px;width:9px;height:9px}
  .brand-main{position:absolute;left:341px;top:840px;display:flex;align-items:center;gap:18px}
  .brand-main .dot{width:148px;height:148px;border-radius:50%;background:var(--navy)}
  .brand-main .rule{width:2px;height:112px;background:var(--red)}
  .brand-main .name{font-weight:900;color:var(--navy);line-height:1}
  .brand-main .name__main{display:block;font-size:70px;letter-spacing:1px}
  .brand-main .name__sub{display:block;font-size:24px;letter-spacing:1px;margin-top:10px}
</style>
</head>
<body>
<section class="stage">
  <article class="card card--front" style="left:125px">
    <div class="brand-mini"><span class="dot"></span>RVQTLO</div>
    <div class="person">
      <div class="person__name">Martin K. Halvey</div>
      <div class="person__title">Principal</div>
    </div>
    <ul class="contact">
      <li><svg viewBox="0 0 10 10"><path d="M5 0a3.5 3.5 0 0 0-3.5 3.5C1.5 6 5 10 5 10s3.5-4 3.5-6.5A3.5 3.5 0 0 0 5 0zm0 5a1.5 1.5 0 1 1 0-3 1.5 1.5 0 0 1 0 3z"/></svg><span><strong>RVQTLO | Response Training Group of NY</strong>Your Company Address Line 1#<br>Company Address Line 2#</span></li>
      <li><svg viewBox="0 0 10 10"><path d="M2 0l2 2.5-1.2 1.3a6 6 0 0 0 3.4 3.4L7.5 6 10 8l-1.5 2C4 10 0 6 0 1.5z"/></svg><span>(+xx) xxx xxx xxx</span></li>
      <li><svg viewBox="0 0 10 10"><path d="M0 2h10v6H0zm1 1v.3l4 2.4 4-2.4V3z"/></svg><span>m.halvey@rvqtlo.com</span></li>
    </ul>
  </article>
  <article class="card card--back" style="left:350px">
    <ul class="services">
      <li>QRB CPR and First Aid Instructors</li>
      <li>Hold the Line Instructors</li>
      <li>Event EMS</li>
      <li>CME's</li>
      <li>MCI Training and Planning</li>
    </ul>
    <div class="brand-center"><span class="dot"></span><span>RVQTLO</span></div>
    <div class="website"><svg viewBox="0 0 10 10" fill="none" stroke="#fff" stroke-width="1"><circle cx="5" cy="5" r="4.3"/><path d="M.7 5h8.6M5 .7c-2.4 2.6-2.4 6 0 8.6M5 .7c2.4 2.6 2.4 6 0 8.6"/></svg>www.rvqtlo.com</div>
  </article>

  <article class="card card--front" style="left:602px">
    <div class="brand-mini"><span class="dot"></span>RVQTLO</div>
    <div class="person">
      <div class="person__name">Owen Tash</div>
      <div class="person__title">Event and Training<br>Specialist</div>
    </div>
    <ul class="contact">
      <li><svg viewBox="0 0 10 10"><path d="M5 0a3.5 3.5 0 0 0-3.5 3.5C1.5 6 5 10 5 10s3.5-4 3.5-6.5A3.5 3.5 0 0 0 5 0zm0 5a1.5 1.5 0 1 1 0-3 1.5 1.5 0 0 1 0 3z"/></svg><span><strong>RVQTLO | Response Training Group of NY</strong>Your Company Address Line 1#<br>Company Address Line 2#</span></li>
      <li><svg viewBox="0 0 10 10"><path d="M2 0l2 2.5-1.2 1.3a6 6 0 0 0 3.4 3.4L7.5 6 10 8l-1.5 2C4 10 0 6 0 1.5z"/></svg><span>(+xx) xxx xxx xxx</span></li>
      <li><svg viewBox="0 0 10 10"><path d="M0 2h10v6H0zm1 1v.3l4 2.4 4-2.4V3z"/></svg><span>o.tash@rvqtlo.com</span></li>
    </ul>
  </article>
  <article class="card card--back" style="left:829px">
    <ul class="services">
      <li>QRB CPR and First Aid Instructors</li>
      <li>Hold the Line Instructors</li>
      <li>Event EMS</li>
      <li>CME's</li>
      <li>MCI Training and Planning</li>
    </ul>
    <div class="brand-center"><span class="dot"></span><span>RVQTLO</span></div>
    <div class="website"><svg viewBox="0 0 10 10" fill="none" stroke="#fff" stroke-width="1"><circle cx="5" cy="5" r="4.3"/><path d="M.7 5h8.6M5 .7c-2.4 2.6-2.4 6 0 8.6M5 .7c2.4 2.6 2.4 6 0 8.6"/></svg>www.rvqtlo.com</div>
  </article>
</section>

<div class="brand-main">
  <span class="dot"></span>
  <span class="rule"></span>
  <span class="name"><span class="name__main">RVQTLO</span><span class="name__sub">RESPONSE TRAINING</span></span>
</div>
</body>
</html>
```